Awesome Podcast Artwork Needed :-)

I need an AWESOME piece of podcast artwork for a new podcast called "Brick By Brick Basics" :-)
The Podcast teaches "new" property investors... or people just starting out... the basics of property investing (real estate) by sharing tips, tricks, strategies, interviews etc.
I have a logo that I'm kind of happy with and have attached examples of it here labelled "Examples Of Logo". It basically consists of four houses hanging on some thread and although I'm certainly not saying you must use it. If you do want to use it, I would be open to you "modernising" it a bit - if needed - or rearranging the house images in a line (horizontally or vertically) or in a square... or indeed in anyway you feel works
In terms of design, I confess I'm really not sure what I want - only I certainly do want to give a sense my Podcast is about "Property Investing".
I have included 2 examples of artwork that my competition uses labelled "Competition Artwork 1&2". I have also included "My Attempt" at doing this... which I know isn't very good - because you can't clearly see the words and to be honest - it looks weak next to other podcast artwork (for example the "Beyond Rental Yields" artwork that I have included here). I have attached a mock up of a "Simulated Podvana Screen" so you can see what I mean when I say my example looks weak compared to the others.
Lastly here's my new website (it's not yet out there) but that may give you some ideas of what I like: https://brickbybrickbasics.com/home/
I'm excited to see what you come up with :-)
PS. The artwork needs to be 3000x3000 pixels with a DPI of 72
Target Market(s)
New property investors - people who want to learn how to invest in property (real estate)
Requirements
Must have
- The name "Brick By Brick Basics"
Nice to have
- If my logo... or a variation on my logo can be incorporated - that would be good - but not essential. I've attached examples but will happily consider modifications.
- Please do not feel however that you must include the logo.

```html
<!DOCTYPE html>
<html lang="en">
<head>
<meta charset="utf-8">
<title>Brick By Brick Basics – Podcast Artwork Options</title>
<link href="https://fonts.googleapis.com/css2?family=Montserrat:wght@400;500;600;700;800&family=Oswald:wght@300;600;700&display=swap" rel="stylesheet">
<style>
  :root {
    --brand-blue: #1a24ff;
    --ink: #111111;
    --paper: #ffffff;
    --frame: #0d0d0d;
    --photo-grey: #d9d9d9;
    --sketch-tint: #f4f4f6;
  }
  * { margin: 0; padding: 0; box-sizing: border-box; }
  html, body { width: 1200px; height: 1200px; overflow: hidden; background: var(--paper); }
  .sheet { position: relative; width: 1200px; height: 1200px; background: var(--paper); }
  .abs { position: absolute; }

  .frame-edge { background: var(--frame); }

  /* Option 1 – typographic cover */
  .cover-type { left: 12px; top: 0; width: 588px; height: 582px; background: var(--paper); overflow: hidden; }
  .cover-type .backdrop { left: 0; top: 0; width: 588px; height: 452px;
    background: linear-gradient(180deg, var(--paper) 0%, var(--sketch-tint) 100%); }
  .headline-stack { font-family: "Montserrat", sans-serif; font-weight: 800; color: var(--brand-blue); letter-spacing: -3px; }
  .cover-type .headline-stack { left: 58px; top: 44px; font-size: 94px; line-height: 92px; }

  .host-band { background: var(--brand-blue); color: var(--paper); font-family: "Montserrat", sans-serif; }
  .cover-type .host-band { left: 0; top: 452px; width: 588px; height: 130px; }
  .host-band .with { font-weight: 500; letter-spacing: 1px; }
  .host-band .host { font-weight: 700; letter-spacing: 0.5px; }
  .host-band .tagline { font-weight: 500; }
  .cover-type .with { left: 36px; top: 33px; font-size: 29px; }
  .cover-type .host { left: 36px; top: 64px; font-size: 40px; }
  .cover-type .tagline { left: 312px; top: 32px; font-size: 14.5px; line-height: 19px; }

  /* Option 2 – host portrait cover */
  .cover-host { left: 611px; top: 0; width: 589px; height: 598px; background: var(--paper); overflow: hidden; }
  .cover-host .backdrop { left: 0; top: 0; width: 589px; height: 458px;
    background: linear-gradient(180deg, var(--paper) 0%, var(--sketch-tint) 100%); }
  .cover-host .portrait { left: 0; top: 12px; width: 281px; height: 446px;
    background: linear-gradient(180deg, #c9ccd2 0%, #3a3f4a 55%, #1f232b 100%); }
  .cover-host .headline-stack { left: 343px; top: 100px; font-size: 62px; line-height: 60px; letter-spacing: -2px; }
  .cover-host .host-band { left: 0; top: 458px; width: 589px; height: 140px; }
  .cover-host .with { left: 48px; top: 47px; font-size: 26px; }
  .cover-host .host { left: 48px; top: 74px; font-size: 37px; }
  .cover-host .tagline { left: 336px; top: 40px; font-size: 13px; line-height: 16.5px; }

  /* Option 3 – photo-led cover */
  .cover-photo { left: 0; top: 584px; width: 602px; height: 616px; background: var(--paper); overflow: hidden; }
  .cover-photo .scene { left: 6px; top: 10px; width: 596px; height: 416px;
    background: linear-gradient(180deg, #b9b3a6 0%, #d8d2c2 40%, #6f8f3a 70%, #3f6a1e 100%); }
  .condensed { font-family: "Oswald", sans-serif; }
  .cover-photo .title { left: 20px; top: 452px; font-weight: 700; font-size: 58px; line-height: 60px; color: var(--ink); letter-spacing: -0.5px; }
  .cover-photo .with { left: 414px; top: 488px; font-weight: 300; font-size: 32px; color: var(--ink); }
  .cover-photo .host { left: 414px; top: 522px; font-weight: 600; font-size: 40px; color: var(--ink); }

  /* Option 4 – aerial city cover */
  .cover-aerial { left: 611px; top: 598px; width: 589px; height: 602px; overflow: hidden;
    background: linear-gradient(160deg, #1b2c78 0%, #0d1a4e 45%, #25357f 75%, #0f1640 100%); }
  .cover-aerial .title-card { left: 131px; top: 244px; width: 458px; height: 284px; background: rgba(255, 255, 255, 0.62); }
  .cover-aerial .title { left: 34px; top: 40px; font-weight: 700; font-size: 64px; line-height: 66px; color: var(--brand-blue); letter-spacing: -0.5px; }
  .cover-aerial .with { left: 180px; top: 208px; font-weight: 300; font-size: 32px; color: var(--brand-blue); }
  .cover-aerial .host { left: 250px; top: 198px; font-weight: 600; font-size: 42px; color: var(--brand-blue); }
</style>
</head>
<body>
<main class="sheet">
  <div class="abs frame-edge" style="left:0;top:0;width:12px;height:582px;"></div>
  <div class="abs frame-edge" style="left:600px;top:0;width:11px;height:598px;"></div>

  <section class="abs cover-type" aria-label="Cover option: typographic">
    <div class="abs backdrop" role="img" aria-label="Faint line sketch of house outlines behind the title"></div>
    <h1 class="abs headline-stack">Brick<br>By<br>Brick<br>Basics</h1>
    <div class="abs host-band">
      <span class="abs with">With</span>
      <span class="abs host">Reid Calder</span>
      <p class="abs tagline">The Basics Of Property Investing<br>By Sharing Tips, Tricks,<br>Strategies And Interviews .</p>
    </div>
  </section>

  <section class="abs cover-host" aria-label="Cover option: host portrait">
    <div class="abs backdrop" role="img" aria-label="Faint line sketch of house outlines behind the title"></div>
    <div class="abs portrait" role="img" aria-label="Photo of the host in a dark suit and light blue shirt"></div>
    <h2 class="abs headline-stack">Brick<br>By<br>Brick<br>Basics</h2>
    <div class="abs host-band">
      <span class="abs with">With</span>
      <span class="abs host">Reid Calder</span>
      <p class="abs tagline">The Basics Of Property Investing<br>By Sharing Tips, Tricks,<br>Strategies And Interviews .</p>
    </div>
  </section>

  <section class="abs cover-photo" aria-label="Cover option: photo-led">
    <div class="abs scene" role="img" aria-label="Photo of a row of four weathered wooden birdhouses on grass"></div>
    <h2 class="abs condensed title">Brick By Brick<br>Basics</h2>
    <span class="abs condensed with">With</span>
    <span class="abs condensed host">Reid Calder</span>
  </section>

  <section class="abs cover-aerial" role="img" aria-label="Aerial photo of a residential street at night, tinted blue">
    <div class="abs title-card">
      <h2 class="abs condensed title">Brick By Brick<br>Basics</h2>
      <span class="abs condensed with">With</span>
      <span class="abs condensed host">Reid Calder</span>
    </div>
  </section>
</main>
</body>
</html>
```